Corvane Sable - Advanced Skincare and undetectable Makeup for Men

We are in need of a professional webpage for our company Corvane Sable. We help every man feel his best by looking his best. Inspired by the myth of Corvane, we offer makeup and skincare products along with education upon their use. Our mission is to celebrate masculinity in all of its forms, regardless of age, race, sexual orientation, or assigned gender at birth.

The webpage would serve as our online store, as a place where our clients can learn about our brand, view our "How-to" video tutorials, and get product information. An online blog will also be hosted in order to keep clients up to date with news, updates, media mentions, etc.

The color schemes that we use are mostly Black and Gold, with Red accents. please keep in mind that this is a men's cosmetics line, and therefore should read powerful, sexy, confident and bold - all with a high end look and feel.

Think along the lines of brands like Len Barrow, QPT, Velcotti, etc.

our logo is included in the files attached. images and copy will be added in at a later time; hence, general images that fit the feel and filler text is encouraged.

The products to be sold include:
a face cleanser in a pump dispenser bottle (1 size)
a mask in a round jar container (1 size)
a moisturizer in a pump container 1 size)
a concealer in a click pen with a brush applicator (3 shades)
a liquid liner pen (4 shades)
a contouring palette (2 shade options)
a setting spray (single option)

Millennial Men

Beauty

5+ page

Serif

ec1f27
000000
faa54b

• ur essential requirements are:
• 1) a stunning and engaging landing page that truly captures the ideals of sexuality, boldness and confidence.
• 2) an interactive and engaging online store that is easy to update / add product / information to.
• 3) Product pages supporting various toggling images of the product, a shade selection option, ingredient information, usage instructions, pricing, and a link to a "how to video" unique to each individual product.
• 4) dedicated space where all of the tutorials can be organized together
• 5) an organized Blog section, that would include a segment for a Q&A section for us to update as the brand grows, ongoing contests (that would be easily hidden if there are no contests running at the moment) as well as general news and updates segment.
• 6) an "about us" page, where our customers are able to learn about our story, inspirations, humanitarian efforts and philosophies in product contents and purity.
• 7) a contact us page, which would include social media links, contact email and telephone number as well as physical address to be updated upon launch.
• 8) discrete privacy policy, terms of use, and return policy links available at the bottom of every page
• 1) A posting forum where clients could post their looks using our products, or maybe a live stream of our Picturloop account.
• 2) a member sign in page so that we can collect and store customer information for faster check out, keep track of purchases attached to their email address (future loyalty program plans) and maintain an email database for email notifications and the such.

```html
<!DOCTYPE html>
<html lang="en">
<head>
<meta charset="utf-8">
<title>Corvane Sable – Men's Cosmetics</title>
<link href="https://fonts.googleapis.com/css2?family=Playfair+Display:wght@700;900&family=Open+Sans:wght@400;600;700&display=swap" rel="stylesheet">
<style>
:root{
  --black:#000;
  --ink:#111;
  --gold:#f2b51c;
  --gold-deep:#c98a12;
  --gold-soft:#faa54b;
  --red:#ec1f27;
  --white:#fff;
  --paper:#f4f4f4;
  --ghost:#efefef;
  --serif:'Playfair Display', Georgia, serif;
  --sans:'Open Sans', Arial, sans-serif;
}
*{box-sizing:border-box;margin:0;padding:0}
html,body{width:1200px;height:4580px;overflow:hidden}
body{position:relative;background:var(--white);font-family:var(--sans);color:var(--ink)}
section,header,footer{position:absolute;left:0;width:1200px;overflow:hidden}
.abs{position:absolute}
.photo{position:absolute}
.gold-title{font-family:var(--serif);font-weight:900;color:var(--gold);text-transform:uppercase;text-align:center;position:absolute;left:0;width:100%}
.ghost-title{font-family:var(--serif);font-weight:900;text-transform:uppercase;text-align:center;position:absolute;left:0;width:100%;font-size:86px;letter-spacing:2px;color:var(--ghost);white-space:nowrap}
.ghost-dark{color:#1a1a1a}

/* Hero */
.hero{top:0;height:545px;background:var(--black)}
.hero-photo{left:300px;top:0;width:620px;height:545px;background:radial-gradient(ellipse 46% 52% at 50% 42%,#9a8577 0%,#6e5c52 28%,#3b3230 52%,#121010 78%,#000 100%)}
.topbar{position:absolute;left:0;top:0;width:100%;height:70px}
.brand{position:absolute;left:290px;top:14px;display:flex;align-items:center;gap:8px;font-family:var(--serif);font-weight:700;color:var(--gold);font-size:15px;letter-spacing:2px}
.brand-mark{width:12px;height:12px;background:var(--gold)}
.info{position:absolute;top:8px;display:flex;gap:6px;color:var(--white);font-size:9px;line-height:12px}
.info svg{flex:none}
.nav{position:absolute;left:520px;top:52px;display:flex;gap:18px;font-size:10px;font-weight:700;color:var(--white)}
.nav .active{color:var(--gold)}
.signup{position:absolute;left:852px;top:0;width:80px;height:24px;background:var(--gold);color:var(--black);font-size:10px;font-weight:700;text-align:center;line-height:24px}
.hero-name{position:absolute;left:150px;top:215px;font-family:var(--serif);font-weight:900;color:var(--gold);font-size:76px;line-height:80px;letter-spacing:1px}
.hero-sub{position:absolute;left:735px;top:232px;font-family:var(--serif);font-weight:900;color:var(--gold);font-size:44px;line-height:52px}

/* About */
.about{top:545px;height:325px;background:var(--black)}
.brush-left{left:0;top:0;width:220px;height:325px;background:radial-gradient(ellipse 45% 55% at 45% 45%,#e0a22a 0%,#8a5a12 30%,#2a1805 60%,#000 80%)}
.brush-right{right:0;top:0;width:220px;height:325px;background:radial-gradient(ellipse 45% 55% at 55% 40%,#e0a22a 0%,#8a5a12 30%,#2a1805 60%,#000 80%)}
.about h2{top:85px;font-size:30px}
.about .lead{position:absolute;top:130px;left:0;width:100%;text-align:center;color:var(--white);font-size:17px}
.about p.body{position:absolute;left:300px;width:600px;color:#ddd;font-size:9.5px;line-height:14px}

/* Categories */
.categories{top:870px;height:820px;background:var(--white)}
.categories .ghost-title{top:0}
.categories h2{top:45px;font-size:34px}
.tile{position:absolute;overflow:hidden}
.tile .photo{inset:0}
.tile::after{content:"";position:absolute;inset:0;background:linear-gradient(180deg,rgba(0,0,0,0) 45%,rgba(0,0,0,.45) 100%)}
.tile span{position:absolute;z-index:1;left:16px;bottom:38px;font-family:var(--serif);font-weight:900;color:var(--white);font-size:16px;text-transform:uppercase}
.tile-r span{left:auto;right:16px}
.tile-m span{left:20px;bottom:14px}

/* Products */
.products{top:1690px;height:910px;background:var(--white)}
.products .ghost-title{top:0}
.products h2{top:52px;font-size:34px}
.card{position:absolute;width:223px}
.card .shot{width:223px;height:311px;position:relative}
.price{position:absolute;right:10px;bottom:14px;background:var(--red);color:var(--white);font-size:13px;font-weight:700;padding:4px 10px}
.card .name{margin-top:14px;font-size:9px;font-weight:600;text-transform:uppercase;color:#222}
.stars{margin-top:6px;display:flex;gap:3px}
.stars i{width:8px;height:8px;border:1px solid #aaa;border-radius:50%}
.brush-side{left:1040px;top:500px;width:160px;height:420px;background:radial-gradient(ellipse 55% 45% at 70% 50%,#8a5a2a 0%,#c49a68 30%,#ecdcc6 55%,#fff 78%)}

/* Videos */
.videos{top:2600px;height:540px;background:var(--black)}
.videos .bg-l{left:0;top:0;width:260px;height:540px;background:radial-gradient(ellipse at 30% 30%,#a06a14 0%,#3a2406 40%,#000 75%)}
.videos .bg-r{right:0;top:0;width:280px;height:540px;background:radial-gradient(ellipse at 70% 35%,#4a3f3a 0%,#151212 50%,#000 80%)}
.videos .ghost-title{top:30px}
.videos h2{top:62px;font-size:34px;color:var(--white)}
.vid{position:absolute}
.play{position:absolute;left:50%;top:50%;border-radius:50%;background:var(--white);transform:translate(-50%,-50%)}
.play::after{content:"";position:absolute;left:42%;top:30%;border-left:12px solid var(--red);border-top:8px solid transparent;border-bottom:8px solid transparent}
.play.sm::after{border-left-width:8px;border-top-width:5px;border-bottom-width:5px;top:31%}
.vid-cap{position:absolute;color:var(--white);font-size:10px;line-height:14px}
.vid-cap.big{font-weight:700;font-size:11px;line-height:15px}

/* Blogs */
.blogs{top:3140px;height:430px;background:var(--white)}
.blogs .ghost-title{top:0}
.blogs h2{top:52px;font-size:34px}
.post{position:absolute;top:127px;width:342px;height:280px}
.post .date{position:absolute;left:18px;top:18px;width:40px;height:44px;background:var(--gold);color:var(--white);text-align:center;font-size:12px;font-weight:700;line-height:16px;padding-top:5px}
.post .by{position:absolute;left:18px;bottom:72px;color:#ddd;font-size:10px}
.post .head{position:absolute;left:18px;right:18px;bottom:26px;color:var(--white);font-size:10px;font-weight:700;line-height:14px;text-transform:uppercase}

/* Follow */
.follow{top:3570px;height:136px;background:var(--white)}
.follow .kicker{position:absolute;top:40px;width:100%;text-align:center;font-family:var(--serif);font-weight:700;font-size:11px;letter-spacing:1px}
.follow .handle{position:absolute;top:56px;width:100%;text-align:center;font-family:var(--serif);font-weight:900;font-size:34px;color:var(--gold);letter-spacing:2px}
.feed{top:3706px;height:220px}
.feed .photo{top:0;height:220px;width:300px}

/* Social */
.social{top:3926px;height:304px;background:var(--black)}
.social .sheen{left:0;top:0;width:1200px;height:304px;background:linear-gradient(115deg,#000 0%,#141414 30%,#000 31%,#0d0d0d 60%,#000 61%)}
.net{position:absolute;top:0;width:220px;height:304px;text-align:center}
.net .mark{position:absolute;left:70px;top:100px;width:80px;height:80px;border:3px solid var(--gold);border-radius:50%}
.net .echo{position:absolute;left:0;width:100%;top:248px;font-family:var(--serif);font-weight:900;color:#1a1a1a;font-size:36px;line-height:44px}
.net .label{position:absolute;left:0;width:100%;top:236px;color:var(--white);font-family:var(--serif);font-weight:700;font-size:12px;letter-spacing:1px}

/* Footer */
.footer{top:4230px;height:350px;background:var(--black)}
.footer .glow{right:0;bottom:0;width:200px;height:350px;background:radial-gradient(ellipse at 70% 70%,#b07818 0%,#3a2508 40%,#000 75%)}
.contact-list{position:absolute;left:245px;top:22px;color:#ddd;font-size:10px;line-height:13px}
.contact-list li{list-style:none;display:flex;gap:12px;margin-bottom:18px}
.contact-list li::before{content:"";width:12px;height:2px;background:var(--gold);margin-top:6px;flex:none}
.form{position:absolute;left:520px;top:16px;width:430px}
.form h3{color:var(--white);font-family:var(--serif);font-weight:700;font-size:16px;letter-spacing:1px;display:flex;gap:10px;align-items:center}
.form h3::before{content:"";width:14px;height:2px;background:var(--gold)}
.form p{color:#ccc;font-size:9px;line-height:13px;margin-top:8px}
.field{border:1px solid #888;height:22px;margin-top:10px;color:#aaa;font-size:9px;padding:5px 8px}
.row{display:flex;gap:12px}
.row .field{flex:1}
.send{margin-top:14px;width:76px;height:22px;background:var(--gold);color:var(--black);font-size:9px;font-weight:700;text-align:center;line-height:22px}
.foot-brand{position:absolute;left:290px;top:272px;display:flex;align-items:center;gap:8px;font-family:var(--serif);font-weight:700;color:var(--gold);font-size:13px;letter-spacing:2px}
.copyright{position:absolute;left:745px;top:278px;color:#bbb;font-size:9px;line-height:13px}
.copyright b{color:var(--gold);font-weight:600}
</style>
</head>
<body>

<header class="hero">
  <div class="photo hero-photo" role="img" aria-label="Portrait of a confident man in a dark shirt against a black background"></div>
  <svg class="abs" style="left:0;top:0" width="1200" height="545" viewBox="0 0 1200 545">
    <line x1="0" y1="130" x2="150" y2="0" stroke="#f2b51c" stroke-width="2"/>
    <line x1="1010" y1="545" x2="1200" y2="380" stroke="#f2b51c" stroke-width="3"/>
    <line x1="1060" y1="545" x2="1200" y2="430" stroke="#c98a12" stroke-width="2"/>
  </svg>
  <div class="topbar">
    <div class="brand"><span class="brand-mark"></span>CORVANE SABLE</div>
    <div class="info" style="left:470px">
      <svg width="12" height="16" viewBox="0 0 12 16"><path d="M6 0C2.7 0 0 2.6 0 5.9 0 10 6 16 6 16s6-6 6-10.1C12 2.6 9.3 0 6 0zm0 8a2 2 0 110-4 2 2 0 010 4z" fill="#f2b51c"/></svg>
      <span>ABC Street City 12345<br>Lorem Ipsum Dolor</span>
    </div>
    <div class="info" style="left:610px">
      <svg width="13" height="13" viewBox="0 0 13 13"><path d="M3 0l2 3-1.3 1.5c.8 1.8 2.1 3.1 3.9 3.9L9 7l3 2-1 3C5.5 12 1 7.5 1 1z" fill="#f2b51c"/></svg>
      <span>Call us<br>+44 000 000 0000</span>
    </div>
    <div class="info" style="left:735px">
      <svg width="14" height="11" viewBox="0 0 14 11"><rect x="0.5" y="0.5" width="13" height="10" fill="none" stroke="#f2b51c"/><path d="M1 1l6 5 6-5" fill="none" stroke="#f2b51c"/></svg>
      <span>Email<br>info@corvanesable.com</span>
    </div>
    <div class="signup">SIGN UP!</div>
    <nav class="nav">
      <span class="active">HOME</span><span>ABOUT</span><span>MAKEUP AND SKINCARE</span><span>PRODUCT</span><span>BLOG</span><span>CONTACT US</span>
      <svg width="14" height="14" viewBox="0 0 14 14"><path d="M2 4h10l-1 9H3z M5 4a2 2 0 014 0" fill="none" stroke="#fff" stroke-width="1.3"/></svg>
    </nav>
  </div>
  <div class="hero-name">CORVANE<br>SABLE</div>
  <div class="hero-sub">MEN'S<br>COSMETICS</div>
</header>

<section class="about">
  <div class="photo brush-left" role="img" aria-label="Makeup brush releasing a cloud of gold powder"></div>
  <div class="photo brush-right" role="img" aria-label="Makeup brush releasing a cloud of gold powder"></div>
  <h2 class="gold-title">About Us</h2>
  <div class="lead">Lorem Ipsum is simply dummy text of the printing and typesetting industry</div>
  <p class="body" style="top:175px">Lorem ipsum has been the industry's standard dummy text ever since the early days, when an unknown printer took a galley of type and scrambled it to make a type specimen book. It has survived not only five decades, but also the leap into electronic typesetting, remaining essentially unchanged. It was popularised with sheets of Lorem Ipsum passages.</p>
  <p class="body" style="top:240px">Lorem ipsum has been the industry's standard dummy text ever since the early days, when an unknown printer took a galley of type and scrambled it to make a type specimen book. It has survived not only five decades, but also the leap into electronic typesetting, remaining essentially unchanged. It was popularised with sheets of Lorem Ipsum passages.</p>
</section>

<section class="categories">
  <div class="ghost-title">Featured Categories</div>
  <h2 class="gold-title">Featured Categories</h2>
  <div class="tile" style="left:0;top:127px;width:372px;height:217px"><div class="photo" style="background:radial-gradient(ellipse at 35% 40%,#c7b59a 0%,#8d8574 40%,#55534f 80%)" role="img" aria-label="Skincare pump containers on a table"></div><span>Pump Container</span></div>
  <div class="tile" style="left:0;top:359px;width:372px;height:217px"><div class="photo" style="background:radial-gradient(ellipse at 40% 35%,#b59a86 0%,#7a6c62 40%,#45403c 85%)" role="img" aria-label="Man applying cream from a round jar"></div><span>Round Jar Container</span></div>
  <div class="tile" style="left:0;top:591px;width:372px;height:217px"><div class="photo" style="background:radial-gradient(ellipse at 60% 45%,#c09a80 0%,#7d6252 40%,#3a2f2a 85%)" role="img" aria-label="Man receiving a facial treatment"></div><span>Liquid Liner Pen</span></div>
  <div class="tile tile-m" style="left:387px;top:127px;width:424px;height:303px"><div class="photo" style="background:radial-gradient(ellipse at 60% 40%,#a38a78 0%,#5d5149 40%,#252120 85%)" role="img" aria-label="Man washing his face with cleanser"></div><span>Face Cleanser</span></div>
  <div class="tile tile-m" style="left:387px;top:445px;width:424px;height:363px"><div class="photo" style="background:radial-gradient(ellipse at 50% 35%,#9c8472 0%,#5b5660 40%,#2a2b30 85%)" role="img" aria-label="Bearded man checking his grooming in a mirror"></div><span>Face Cleaner Bottle</span></div>
  <div class="tile tile-r" style="left:826px;top:127px;width:374px;height:217px"><div class="photo" style="background:radial-gradient(ellipse at 50% 50%,#d6d2cc 0%,#a6a29d 45%,#6e6b68 90%)" role="img" aria-label="Flat lay of makeup brushes and pens"></div><span>Liquid Liner Pen</span></div>
  <div class="tile tile-r" style="left:826px;top:359px;width:374px;height:217px"><div class="photo" style="background:radial-gradient(ellipse at 45% 50%,#c48f70 0%,#8a5e48 40%,#4a342b 85%)" role="img" aria-label="Assorted powder compacts"></div><span>Click Pen</span></div>
  <div class="tile tile-r" style="left:826px;top:591px;width:374px;height:217px"><div class="photo" style="background:radial-gradient(ellipse at 55% 45%,#9a7d9a 0%,#6a5565 40%,#3a3038 85%)" role="img" aria-label="Makeup sponge and contouring tools"></div><span>Contouring Palette</span></div>
</section>

<section class="products">
  <div class="ghost-title">Our Products</div>
  <h2 class="gold-title">Our Products</h2>
  <div class="photo brush-side" role="img" aria-label="Bundle of makeup brushes"></div>
  <div class="card" style="left:250px;top:149px"><div class="shot" style="background:radial-gradient(ellipse 30% 40% at 50% 48%,#d9852a 0%,#eab47a 45%,#f4f4f4 100%)" role="img" aria-label="Amber face cleanser pump bottle"><span class="price">$30.00</span></div><div class="name">A face cleanser in a pump dispenser bottle</div><div class="stars"><i></i><i></i><i></i><i></i><i></i></div></div>
  <div class="card" style="left:488px;top:149px"><div class="shot" style="background:radial-gradient(ellipse 32% 22% at 50% 48%,#cfd3d6 0%,#e4e6e8 50%,#f4f4f4 100%)" role="img" aria-label="Clear round jar with black lid"><span class="price">$30.00</span></div><div class="name">A mask in a round jar container</div><div class="stars"><i></i><i></i><i></i><i></i><i></i></div></div>
  <div class="card" style="left:726px;top:149px"><div class="shot" style="background:radial-gradient(ellipse 22% 40% at 50% 50%,#ffffff 0%,#e9e9e9 50%,#f4f4f4 100%)" role="img" aria-label="White moisturizer pump bottle"><span class="price">$30.00</span></div><div class="name">A moisturizer in a pump container</div><div class="stars"><i></i><i></i><i></i><i></i><i></i></div></div>
  <div class="card" style="left:250px;top:506px"><div class="shot" style="background:radial-gradient(ellipse 14% 42% at 50% 48%,#3a3a3a 0%,#b0a070 40%,#f4f4f4 100%)" role="img" aria-label="Concealer click pen with brush tip"><span class="price">$30.00</span></div><div class="name">A concealer in a click pen with a brush</div><div class="stars"><i></i><i></i><i></i><i></i><i></i></div></div>
  <div class="card" style="left:488px;top:506px"><div class="shot" style="background:radial-gradient(ellipse 12% 42% at 50% 48%,#1a1a1a 0%,#8a8a8a 45%,#f4f4f4 100%)" role="img" aria-label="Black liquid liner pen"><span class="price">$30.00</span></div><div class="name">A liquid liner pen</div><div class="stars"><i></i><i></i><i></i><i></i><i></i></div></div>
  <div class="card" style="left:726px;top:506px"><div class="shot" style="background:radial-gradient(ellipse 40% 26% at 50% 46%,#7a5038 0%,#3a2a24 40%,#c9bdb4 70%,#f4f4f4 100%)" role="img" aria-label="Contouring palette with six shades"><span class="price">$30.00</span></div><div class="name">A contouring palette</div><div class="stars"><i></i><i></i><i></i><i></i><i></i></div></div>
</section>

<section class="videos">
  <div class="photo bg-l" role="img" aria-label="Brush with gold powder burst"></div>
  <div class="photo bg-r" role="img" aria-label="Bearded man in shadow"></div>
  <div class="ghost-title ghost-dark">Our Videos</div>
  <h2 class="gold-title">Our Videos</h2>
  <div class="vid" style="left:250px;top:155px;width:360px;height:258px;background:radial-gradient(ellipse at 65% 40%,#c4a88e 0%,#8a7766 35%,#4a4644 80%)" role="img" aria-label="Tutorial video still of a man grooming"><div class="play" style="width:56px;height:56px"></div></div>
  <div class="vid-cap" style="left:285px;top:425px;font-size:9px">24 Aug 2024</div>
  <div class="vid-cap big" style="left:285px;top:443px;width:300px">Lorem ipsum is simply dummy text of the printing and typesetting industry. Lorem Ipsum has been the standard.</div>
  <div class="vid" style="left:625px;top:155px;width:147px;height:113px;background:radial-gradient(ellipse at 50% 40%,#b99c86 0%,#6e6058 50%,#353130 95%)" role="img" aria-label="Video still of skincare routine"><div class="play sm" style="width:30px;height:30px"></div></div>
  <div class="vid" style="left:793px;top:155px;width:156px;height:113px;background:radial-gradient(ellipse at 50% 40%,#a4a8ad 0%,#6a6e73 50%,#33363a 95%)" role="img" aria-label="Video still of skincare routine"><div class="play sm" style="width:30px;height:30px"></div></div>
  <div class="vid-cap" style="left:625px;top:278px;width:150px">Lorem Ipsum is simply dummy text of the printing</div>
  <div class="vid-cap" style="left:793px;top:278px;width:156px">Lorem Ipsum is simply dummy text of the printing</div>
  <div class="vid" style="left:625px;top:325px;width:147px;height:113px;background:radial-gradient(ellipse at 50% 45%,#c7a48a 0%,#7d6758 50%,#3a302b 95%)" role="img" aria-label="Video still of makeup application"><div class="play sm" style="width:30px;height:30px"></div></div>
  <div class="vid" style="left:793px;top:325px;width:156px;height:113px;background:radial-gradient(ellipse at 50% 45%,#b89478 0%,#6d5a4e 50%,#322a26 95%)" role="img" aria-label="Video still of makeup application"><div class="play sm" style="width:30px;height:30px"></div></div>
  <div class="vid-cap" style="left:625px;top:448px;width:150px">Lorem Ipsum is simply dummy text of the printing</div>
  <div class="vid-cap" style="left:793px;top:448px;width:156px">Lorem Ipsum is simply dummy text of the printing</div>
</section>

<section class="blogs">
  <div class="ghost-title">Latest Blogs</div>
  <h2 class="gold-title">Latest Blogs</h2>
  <article class="post" style="left:250px;background:linear-gradient(180deg,rgba(0,0,0,0) 45%,rgba(0,0,0,.7) 100%),radial-gradient(ellipse at 45% 40%,#9a7d9a 0%,#7a5a3e 40%,#2e2522 90%)" role="img" aria-label="Makeup sponge and brush on a dark table">
    <div class="date">22<br>Aug</div>
    <div class="by">By Admin</div>
    <div class="head">Lorem ipsum is simply dummy text of the printing and typesetting industry lorem ipsum text.</div>
  </article>
  <article class="post" style="left:607px;background:linear-gradient(180deg,rgba(0,0,0,0) 45%,rgba(0,0,0,.7) 100%),radial-gradient(ellipse at 50% 35%,#b49a86 0%,#6e6870 40%,#2a2b30 90%)" role="img" aria-label="Bearded man in a barbershop">
    <div class="date">22<br>Aug</div>
    <div class="by">By Admin</div>
    <div class="head">Lorem ipsum is simply dummy text of the printing and typesetting industry lorem ipsum text.</div>
  </article>
</section>

<section class="follow">
  <div class="kicker">FOLLOW ME ON PICTURLOOP</div>
  <div class="handle">CORVANE_SABLE</div>
</section>

<section class="feed">
  <div class="photo" style="left:0;background:radial-gradient(ellipse at 45% 50%,#e0bfa4 0%,#b08c72 45%,#6f5646 95%)" role="img" aria-label="Man receiving a facial massage"></div>
  <div class="photo" style="left:300px;background:radial-gradient(ellipse at 50% 45%,#c9ab95 0%,#8e8a88 45%,#5a5d62 95%)" role="img" aria-label="Man applying skincare"></div>
  <div class="photo" style="left:600px;background:radial-gradient(ellipse at 45% 50%,#b08aa8 0%,#7a5a44 45%,#3a2e2a 95%)" role="img" aria-label="Makeup sponge and brushes"></div>
  <div class="photo" style="left:900px;background:radial-gradient(ellipse at 55% 45%,#e2b89a 0%,#a9b8c4 50%,#6f8494 95%)" role="img" aria-label="Smiling man applying moisturizer"></div>
</section>

<section class="social">
  <div class="photo sheen" role="img" aria-label="Dark angled light bands"></div>
  <div class="net" style="left:180px"><div class="mark"></div><div class="echo">FRIEND</div><div class="label">FRIENDGRID</div></div>
  <div class="net" style="left:490px"><div class="mark"></div><div class="echo">CHIRP</div><div class="label">CHIRPWIRE</div></div>
  <div class="net" style="left:800px"><div class="mark"></div><div class="echo">PICTUR</div><div class="label">PICTURLOOP</div></div>
</section>

<footer class="footer">
  <div class="photo glow" role="img" aria-label="Brush with gold powder burst"></div>
  <ul class="contact-list">
    <li><span>ABC Street City 12345<br>Lorem ipsum is simply dummy</span></li>
    <li><span>Call us<br>+44 000 000 0000</span></li>
    <li><span>Email<br>info@corvanesable.com</span></li>
    <li><span>Website<br>www.corvanesable.com</span></li>
  </ul>
  <div class="form">
    <h3>CONTACT US</h3>
    <p>Lorem ipsum is simply dummy text of the printing and typesetting industry. Lorem Ipsum has been the industry's standard dummy text ever since the early days, when an unknown printer took a galley of type and scrambled it.</p>
    <div class="field">Email</div>
    <div class="row"><div class="field">First Name</div><div class="field">Last Name</div></div>
    <div class="send">SIGN UP</div>
  </div>
  <div class="foot-brand"><span class="brand-mark"></span>CORVANE SABLE</div>
  <div class="copyright">Copyright © 2024 <b>Corvane Sable</b>. All rights reserved.<br>Privacy Policy · Terms of Use · Returns</div>
</footer>

</body>
</html>
```